Corporate brochure design 4 pages

Hi,

We are a real estate company based in Europe.

We have almost finalized a rebranding.

We are developing a brand book guidelines (still on working process) to help you undertstand the look and feel of our new CI. I would like to receive proposals of design for a corporate brochure template. I need to receive the Indesign files with full ownership rights to be able to adapt all our documentation with this template.
Regarding the images, you can take gabaris on www.pelvaromedia.com. I will be able to take them afterwards.

There will be 4 pages. you will receive the 4 pages on pdf for your consideration with our (almost) actual layout.

- 1st page: cover
- 2nd page: company presentation in french and english
- 3rd page: some market data + graph
- 4th page: 2 retail centers presentation.

In the template, i need to have:
- the paragraph styles in order
- 2 different masters with top/bottom/page number aso.

Please feel free to ask any other questions.

best regards,
Updates

I would like to precise tha t we are active on the commercial real estate sector:

- office transactions (rent /sales)
- property management of administrative and business buildings
- Valuation of properties
- Capital markets (investment advices for selling building)

Industry/Entity Type

Real Estate

Colors

Designer to choose colors to be used in the design.

```html
<!DOCTYPE html>
<html lang="en">
<head>
<meta charset="utf-8">
<title>Market Data &amp; Graph</title>
<link rel="stylesheet" href="https://fonts.googleapis.com/css2?family=Arimo:wght@400;700&display=swap">
<style>
  :root {
    --orange: #f2711c;
    --cell: #fdeee6;
    --black: #111111;
    --navy: #1f3f7a;
    --grey: #555555;
    --label-red: #d63a2a;
    --white: #ffffff;
  }
  html, body { margin: 0; padding: 0; overflow: hidden; }
  body { background: var(--white); }
  .page {
    position: relative; width: 848px; height: 1200px; overflow: hidden;
    background: var(--white); font-family: "Arimo", Arial, sans-serif; color: var(--black);
  }
  .band { position: absolute; left: 0; width: 848px; }
  .band--top { top: 0; height: 82px; }
  .band--top .band__orange { position: absolute; left: 0; top: 0; width: 100%; height: 30px; background: var(--orange); }
  .band--top .band__black { position: absolute; left: 0; top: 38px; width: 100%; height: 10px; background: var(--black); }
  .band--top .band__rule { position: absolute; left: 0; top: 80px; width: 100%; height: 2px; background: var(--black); }
  .band--bottom { bottom: 0; height: 58px; }
  .band--bottom .band__orange { position: absolute; left: 0; top: 0; width: 100%; height: 8px; background: var(--orange); }
  .band--bottom .band__black { position: absolute; left: 0; top: 14px; width: 100%; height: 44px; background: var(--black); }
  .band--bottom .band__stripe { position: absolute; left: 0; top: 36px; width: 100%; height: 6px; background: var(--orange); }
  .backdrop {
    position: absolute; left: 330px; top: 150px; width: 518px; height: 960px;
    background: radial-gradient(ellipse at 60% 60%, rgba(242,113,28,0.10), rgba(242,113,28,0) 65%);
  }
  .title-pill {
    position: absolute; left: 281px; top: 66px; width: 289px; height: 31px;
    background: var(--black); color: var(--white); border-radius: 16px;
    font-weight: 700; font-size: 20px; letter-spacing: 0.5px;
    display: flex; align-items: center; justify-content: center;
  }
  .intro { position: absolute; top: 118px; }
  .intro--fr { left: 48px; width: 375px; }
  .intro--en { left: 445px; width: 354px; }
  .intro__label { font-size: 11.5px; font-weight: 700; margin: 0; }
  .intro__heading { font-size: 25px; font-weight: 400; margin: 3px 0 1px; line-height: 28px; }
  .intro__body { font-size: 16.5px; font-weight: 700; line-height: 20.5px; margin: 0; color: #222; text-align: justify; }
  .stock-table {
    position: absolute; left: 26px; top: 272px; width: 798px;
    border-collapse: separate; border-spacing: 0 2px; font-size: 12.5px; table-layout: fixed;
  }
  .stock-table th, .stock-table td { height: 23px; padding: 0 6px; white-space: nowrap; }
  .stock-table th { font-weight: 700; font-size: 12px; text-align: left; }
  .stock-table .num { text-align: right; }
  .stock-table td.cell { background: var(--cell); }
  .stock-table td.region { font-weight: 700; font-size: 13px; }
  .stock-table tr.total td { font-weight: 700; }
  .stock-table tr.total td.label { text-align: right; padding-right: 24px; }
  .stock-table .pct { padding-right: 24px; }
  .grand-total {
    position: absolute; left: 26px; top: 879px; width: 798px; height: 24px;
    background: var(--cell); font-size: 13px; font-weight: 700;
  }
  .grand-total span { position: absolute; top: 5px; }
  .chart { position: absolute; left: 220px; top: 908px; width: 420px; height: 215px; }
</style>
</head>
<body>
<div class="page">

  <div class="band band--top" aria-hidden="true">
    <div class="band__orange"></div><div class="band__black"></div><div class="band__rule"></div>
  </div>

  <div class="backdrop" role="img" aria-label="Fine flowing orange line pattern in the background"></div>

  <div class="title-pill">MARKET DATA &amp; GRAPH</div>

  <section class="intro intro--fr" lang="fr">
    <p class="intro__label">RAPPORT DE MARCHÉ BUREAUX LUXEMBOURG Q3-2013</p>
    <h2 class="intro__heading">STOCK</h2>
    <p class="intro__body">Le stock de mètres carrés disponibles de bureaux a augmenté de 0,36 % au troisième trimestre de cette année grâce à la livraison de près de 12 300 m². Le stock total équivaut à 3 465 600 m².</p>
  </section>

  <section class="intro intro--en">
    <p class="intro__label">LUXEMBOURG OFFICE MARKET REPORT Q3-2013</p>
    <h2 class="intro__heading">STOCK</h2>
    <p class="intro__body">The stock of available office square meters has increased by 0.36% during the third quarter of this year with the delivery of 12,300 m². The total stock reaches 3,465,600 sm².</p>
  </section>

  <table class="stock-table">
    <colgroup><col style="width:323px"><col style="width:199px"><col style="width:117px"><col style="width:159px"></colgroup>
    <thead>
      <tr><th></th><th>QUARTIERS-DISTRICTS</th><th class="num">STOCK M²</th><th class="num pct">STOCK %</th></tr>
    </thead>
    <tbody>
      <tr><td class="region cell">CENTRE-VILLE (CITY)</td><td class="cell">Kirchberg</td><td class="cell num">915 000</td><td class="cell num pct">26,42 %</td></tr>
      <tr><td></td><td class="cell">CBD</td><td class="cell num">806 400</td><td class="cell num pct">23,27 %</td></tr>
      <tr><td></td><td class="cell">Station</td><td class="cell num">382 700</td><td class="cell num pct">11,04 %</td></tr>
      <tr><td></td><td class="cell">Cloche d'Or</td><td class="cell num">365 600</td><td class="cell num pct">10,55 %</td></tr>
      <tr><td></td><td class="cell">Limpertsberg</td><td class="cell num">85 000</td><td class="cell num pct">2,45 %</td></tr>
      <tr><td></td><td class="cell">Belair / Merl</td><td class="cell num">67 800</td><td class="cell num pct">1,96 %</td></tr>
      <tr><td></td><td class="cell">Hamm</td><td class="cell num">44 500</td><td class="cell num pct">1,28 %</td></tr>
      <tr><td></td><td class="cell">Kalchesbrück</td><td class="cell num">33 000</td><td class="cell num pct">0,95 %</td></tr>
      <tr class="total"><td></td><td class="label">TOTAL</td><td class="cell num">2 700 500</td><td class="cell num pct">77,92 %</td></tr>
      <tr><td class="region cell">VILLE-PÉRIPHÉRIE (CITY-PERIPHERY)</td><td class="cell">Airport - Findel</td><td class="cell num">157 500</td><td class="cell num pct">4,54 %</td></tr>
      <tr><td></td><td class="cell">Bertrange / Bourmicht</td><td class="cell num">82 000</td><td class="cell num pct">2,37 %</td></tr>
      <tr><td></td><td class="cell">Strassen</td><td class="cell num">81 050</td><td class="cell num pct">2,34 %</td></tr>
      <tr><td></td><td class="cell">Howald</td><td class="cell num">62 600</td><td class="cell num pct">1,81 %</td></tr>
      <tr class="total"><td></td><td class="label">TOTAL</td><td class="cell num">383 150</td><td class="cell num pct">11,06 %</td></tr>
      <tr><td class="region cell">PÉRIPHÉRIE (PERIPHERY)</td><td class="cell">Belval</td><td class="cell num">93 090</td><td class="cell num pct">2,69 %</td></tr>
      <tr><td></td><td class="cell">Capellen</td><td class="cell num">69 500</td><td class="cell num pct">2,01 %</td></tr>
      <tr><td></td><td class="cell">Leudelange</td><td class="cell num">73 556</td><td class="cell num pct">2,12 %</td></tr>
      <tr><td></td><td class="cell">Munsbach</td><td class="cell num">60 100</td><td class="cell num pct">1,73 %</td></tr>
      <tr><td></td><td class="cell">Windhof</td><td class="cell num">40 600</td><td class="cell num pct">1,17 %</td></tr>
      <tr><td></td><td class="cell">Esch-sur-Alzette</td><td class="cell num">24 700</td><td class="cell num pct">0,71 %</td></tr>
      <tr><td></td><td class="cell">Contern</td><td class="cell num">20 400</td><td class="cell num pct">0,59 %</td></tr>
      <tr class="total"><td></td><td class="label">TOTAL</td><td class="cell num">381 946</td><td class="cell num pct">11,02 %</td></tr>
    </tbody>
  </table>

  <div class="grand-total"><span style="left:270px">TOTAL</span><span style="left:584px">3 465 596</span></div>

  <svg class="chart" viewBox="220 908 420 215" aria-label="Office stock by year, 2003 to YTD 2013">
    <text x="498" y="921" font-size="10" text-anchor="middle" fill="var(--grey)" font-family="Arimo, sans-serif">Source: Meridia Estates Research</text>
    <g font-family="Arimo, sans-serif" font-size="6" fill="var(--grey)" text-anchor="end">
      <text x="255" y="1087">1,700</text><text x="255" y="1066">2,000</text><text x="255" y="1044">2,300</text>
      <text x="255" y="1023">2,600</text><text x="255" y="1001">2,900</text><text x="255" y="980">3,200</text>
      <text x="255" y="958">3,500</text><text x="255" y="937">3,800</text>
    </g>
    <line x1="260" y1="1085" x2="620" y2="1085" stroke="#888" stroke-width="0.8"/>
    <line x1="260" y1="935" x2="260" y2="1085" stroke="#888" stroke-width="0.8"/>
    <g fill="var(--navy)">
      <rect x="265" y="1045.6" width="23" height="39.4"/>
      <rect x="298" y="1035" width="23" height="50"/>
      <rect x="330" y="1027.6" width="23" height="57.4"/>
      <rect x="363" y="1020.7" width="23" height="64.3"/>
      <rect x="396" y="1013.6" width="23" height="71.4"/>
      <rect x="429" y="998.4" width="23" height="86.6"/>
      <rect x="461" y="982.3" width="23" height="102.7"/>
      <rect x="494" y="971.1" width="23" height="113.9"/>
      <rect x="527" y="967.1" width="23" height="117.9"/>
      <rect x="559" y="963.1" width="23" height="121.9"/>
      <rect x="592" y="958.9" width="23" height="126.1"/>
    </g>
    <g font-family="Arimo, sans-serif" font-size="5.5" fill="var(--label-red)" text-anchor="middle">
      <text x="276" y="1042">2,251</text><text x="309" y="1032">2,400</text><text x="341" y="1024">2,504</text>
      <text x="374" y="1017">2,600</text><text x="407" y="1010">2,700</text><text x="440" y="995">2,912</text>
      <text x="472" y="979">3,138</text><text x="505" y="968">3,295</text><text x="538" y="964">3,351</text>
      <text x="570" y="960">3,406</text><text x="603" y="956">3,466</text>
    </g>
    <g font-family="Arimo, sans-serif" font-size="5.5" fill="var(--grey)" text-anchor="middle">
      <text x="276" y="1095">2003</text><text x="309" y="1095">2004</text><text x="341" y="1095">2005</text>
      <text x="374" y="1095">2006</text><text x="407" y="1095">2007</text><text x="440" y="1095">2008</text>
      <text x="472" y="1095">2009</text><text x="505" y="1095">2010</text><text x="538" y="1095">2011</text>
      <text x="570" y="1095">2012</text><text x="603" y="1095">YTD 2013</text>
    </g>
    <rect x="550" y="1106" width="78" height="16" fill="none" stroke="#bbb" stroke-width="0.6"/>
    <rect x="578" y="1108" width="46" height="7" fill="var(--navy)"/>
    <text x="555" y="1120" font-family="Arimo, sans-serif" font-size="5" fill="var(--grey)">Stock</text>
  </svg>

  <div class="band band--bottom" aria-hidden="true">
    <div class="band__orange"></div><div class="band__black"></div><div class="band__stripe"></div>
  </div>

</div>
</body>
</html>
```